Business card design for engineering firm specializing in defense industry.

We need a professional business card design. Something simple but stands out. We are an engineering company specializing in composites in the defense industry.
Industry/Entity Type
Defense
Contact Information for Business Card
A simple black business card with the Varlonix yellow color is what we had in mind but open for other designs.
Colors
ffc214

```html
<!DOCTYPE html>
<html lang="en">
<head>
<meta charset="utf-8">
<title>Varlonix Business Card</title>
<link href="https://fonts.googleapis.com/css2?family=Lato:wght@400;700;900&display=swap" rel="stylesheet">
<style>
  :root {
    --backdrop: #141414;
    --card-dark: #232323;
    --brand-yellow: #ffc214;
    --paper: #ffffff;
    --ink-light: #ffffff;
  }
  * { margin: 0; padding: 0; box-sizing: border-box; }
  html, body {
    width: 1200px; height: 912px; overflow: hidden;
    background: var(--backdrop);
    font-family: "Lato", sans-serif;
  }
  .stage {
    width: 1200px; height: 912px;
    display: flex; flex-direction: column;
    align-items: center; justify-content: center; gap: 40px;
  }
  .card {
    width: 700px; height: 400px; position: relative; overflow: hidden;
  }

  /* Front */
  .card-front {
    background: linear-gradient(160deg, #2c2c2c 0%, var(--card-dark) 55%, #1d1d1d 100%);
    display: flex; flex-direction: column; align-items: center; justify-content: center;
  }
  .brand {
    display: flex; align-items: center; gap: 18px;
  }
  .brand-mark {
    width: 46px; height: 46px; background: var(--brand-yellow);
  }
  .brand-name {
    font-weight: 900; font-size: 72px; color: var(--ink-light); letter-spacing: 1px;
  }
  .front-web {
    margin-top: 40px; font-size: 17px; color: var(--ink-light); letter-spacing: 0.5px;
  }

  /* Back */
  .card-back { background: var(--paper); }
  .band {
    position: absolute; top: 82px; height: 236px;
  }
  .name-panel {
    left: 0; width: 256px; background: var(--card-dark);
    display: flex; flex-direction: column; align-items: flex-end; justify-content: center;
    padding-right: 22px;
  }
  .person-name {
    font-size: 25px; font-weight: 700; color: var(--brand-yellow); white-space: nowrap;
  }
  .person-role {
    font-size: 16px; color: var(--ink-light); margin-top: 2px;
  }
  .contact-panel {
    left: 266px; right: 0; background: var(--brand-yellow);
    padding: 34px 0 0 42px;
  }
  .divider {
    position: absolute; left: 30px; top: 34px; bottom: 30px;
    width: 2px; background: var(--ink-light);
  }
  .address {
    font-size: 15px; line-height: 20px; color: var(--ink-light); padding-left: 30px;
  }
  .contact-list {
    list-style: none; margin-top: 18px;
  }
  .contact-list li {
    display: flex; align-items: center; gap: 12px;
    font-size: 15px; line-height: 22px; color: var(--ink-light);
  }
  .contact-list svg { width: 16px; height: 16px; flex: none; fill: var(--ink-light); }
</style>
</head>
<body>
<main class="stage">
  <section class="card card-front">
    <div class="brand">
      <span class="brand-mark"></span>
      <span class="brand-name">Varlonix</span>
    </div>
    <p class="front-web">www.varlonixinc.com</p>
  </section>

  <section class="card card-back">
    <div class="band name-panel">
      <p class="person-name">Daniel Hartwell</p>
      <p class="person-role">Manager</p>
    </div>
    <div class="band contact-panel">
      <span class="divider"></span>
      <p class="address">18 Harlow Avenue<br>Dalton, Maine 04630</p>
      <ul class="contact-list">
        <li>
          <svg viewBox="0 0 16 16"><path d="M3.5 1.5l2.5 0 1 3.5-1.8 1.2a8 8 0 0 0 4.6 4.6l1.2-1.8 3.5 1v2.5c0 .8-.7 1.5-1.5 1.5A12.5 12.5 0 0 1 2 3c0-.8.7-1.5 1.5-1.5z"/></svg>
          555 014 2200
        </li>
        <li>
          <svg viewBox="0 0 16 16"><rect x="4" y="1.5" width="8" height="4"/><rect x="1.5" y="6" width="13" height="6" rx="1"/><rect x="4" y="10" width="8" height="4.5" fill="#ffc214" stroke="#fff" stroke-width="1.2"/></svg>
          555 014 2201
        </li>
        <li>
          <svg viewBox="0 0 16 16"><rect x="1.5" y="3.5" width="13" height="9" rx="1"/><path d="M2 4l6 5 6-5" fill="none" stroke="#ffc214" stroke-width="1.3"/></svg>
          info@varlonixinc.com
        </li>
        <li>
          <svg viewBox="0 0 16 16"><circle cx="8" cy="8" r="6.5"/><path d="M1.5 8h13M8 1.5c-2.5 3-2.5 10 0 13M8 1.5c2.5 3 2.5 10 0 13" fill="none" stroke="#ffc214" stroke-width="1"/></svg>
          www.varlonixinc.com
        </li>
      </ul>
    </div>
  </section>
</main>
</body>
</html>
```